Business Card Needed for Crafter of Pottery, Jewelry and Artwork

Calling all designers in search of an artistic challenge.

I need a new business card design for my pottery, jewelry and artwork business, Woven Glass and Tide, based in Vancouver BC.

I would like a card that is bright and inviting and preferably incorporates my logo and a sample of photos of my work while having a clean fresh look. The following contact details would preferably be included on the card as well:
• Helena Pikeworth
• Designer
• Phone: 604.555.0172
• Email: Designer@WovenGlassandTide.example
• Website: www.WovenGlassandTide.example
• Blog: www.ShapingHillside.example

The logo is attached in two color schemes in both Vector and Source formats. On past cards I’ve also included photos of my work. By including photos of the work the pieces are showcased and it catches people’s eye and prompts them to pick up the card and look at it more closely. For example, if I leave a stack in a coffee shop I want people to be drawn to the card, to pick it up and get a sense of the my product lines. Please feel free to pull photos of my work directly off of my website. If you need photos with higher pixels please let me know and I’ll email them directly to you. The website background is bffbda (191, 251, 218). I would like the business cards to match the feel of the website for consistency but the cards do not need to use the exact same colors. My website and current business card are predominantly turquoise shades. The background uses stripes provided by the website template. I don’t know the exact colors of the stripes.

My current business card is attached to show the use of photos in a design. Please note that I am not thrilled with my own design and am looking for variations and completely new designs. This example is not meant to be used as a template or starting point.

Here is some background surrounding my company:
WGT offers one of a kind jewelry, pottery, artwork and leather bags each designed with a twist. The pottery varies from rustic every day functional ware to raku artwork. The jewelry ranges from simple sterling every day pieces to multimedia pieces incorporating stone, metal, ceramics and fabric. The artwork is multimedia, typically acrylic paired with a natural element such as bark. All the bags are leather with reworked kimono fabric or patterned silk lining.

Feel free to check out my website to get a flavour for my work and the color scheme I've used on marketing materials so far. www.wovenglassandtide.example
Updates

Thank you to everyone who has submitted a design so far. I hope everyone has received some helpful feedback.

I'm going to post a survey to customers and friends asking for their votes. If you have new designs to submit please try to get them in by Saturday March 30 at noon so that I can include it in the survey launch.

Thank you

Target Market(s)

Females aged 25-65 interested in one of a kind functional pottery and jewelry.

Industry/Entity Type

Coffee Shop

Requirements
Must have
• Contact information, website, blog
Nice to have
• Logo, photos

```html
<!DOCTYPE html>
<html lang="en">
<head>
<meta charset="utf-8">
<title>Woven Glass and Tide — Business Cards</title>
<link rel="stylesheet" href="https://fonts.googleapis.com/css2?family=Cardo:wght@400;700&display=swap">
<style>
  :root {
    --page-bg: #eef1f0;
    --turquoise: #3cc2c2;
    --turquoise-deep: #2aa9ab;
    --mint: #c9f3e6;
    --mint-light: #dcf8ee;
    --teal-text: #1f9b8e;
    --navy: #2d2f6e;
    --ink: #1d1d1d;
    --white: #ffffff;
    --rule: #2a2a2a;
  }
  * { box-sizing: border-box; margin: 0; padding: 0; }
  html, body { width: 1200px; height: 1000px; overflow: hidden; }
  body {
    background: var(--page-bg);
    font-family: "Cardo", Georgia, serif;
    position: relative;
  }
  .card {
    position: absolute;
    width: 540px;
    height: 310px;
    overflow: hidden;
    box-shadow: 0 6px 18px rgba(0,0,0,0.18);
  }

  /* ---------- Front card ---------- */
  .card-front { left: 50px; top: 230px; background: var(--mint); }
  .front-showcase {
    position: absolute; left: 0; top: 0; width: 100%; height: 200px;
    background: linear-gradient(180deg, var(--turquoise) 0%, var(--turquoise-deep) 100%);
  }
  .front-band {
    position: absolute; left: 0; top: 200px; width: 100%; height: 10px;
    background: var(--white);
  }
  .front-url {
    position: absolute; left: 0; right: 0; top: 236px;
    text-align: center; font-weight: 700; font-size: 28px;
    color: var(--teal-text);
  }
  .work-photo {
    position: absolute; border: 3px solid rgba(255,255,255,0.75); border-radius: 4px;
  }
  .photo-bag { left: 290px; top: 14px; width: 130px; height: 60px; background: linear-gradient(135deg,#f0ece4,#d9a84a); }
  .photo-bowl { left: 170px; top: 48px; width: 110px; height: 80px; background: linear-gradient(135deg,#f2ede6,#6b4d3c); }
  .photo-pottery { left: 300px; top: 84px; width: 140px; height: 100px; background: linear-gradient(160deg,#8a5a2c,#3aa585 70%,#2b2b2b); }
  .photo-necklace { left: 170px; top: 136px; width: 120px; height: 60px; background: linear-gradient(135deg,#efe9e4,#9a5a2e 60%,#8fcf7a); }

  .brand-mark {
    position: absolute; width: 118px; height: 118px; border-radius: 50%;
    background: var(--white); border: 4px solid var(--turquoise-deep);
    display: flex; align-items: center; justify-content: center; text-align: center;
    font-weight: 700; font-size: 15px; line-height: 1.15; color: var(--navy);
    padding: 12px;
  }
  .card-front .brand-mark { left: 26px; top: 120px; }

  /* ---------- Back card ---------- */
  .card-back { left: 620px; top: 430px; background: linear-gradient(180deg, var(--mint-light), var(--mint)); }
  .card-back .brand-mark {
    left: 52px; top: 30px; background: var(--turquoise); border: 4px solid var(--white);
    color: var(--white);
  }
  .holder-name {
    position: absolute; left: 220px; top: 32px;
    font-weight: 700; font-size: 34px; color: var(--teal-text);
  }
  .holder-title {
    position: absolute; left: 400px; top: 74px;
    font-size: 13px; color: var(--teal-text);
  }
  .contact-list {
    position: absolute; left: 196px; top: 98px; list-style: none;
    font-weight: 700; font-size: 16px; color: var(--ink);
  }
  .contact-list li { display: flex; align-items: center; gap: 8px; height: 26px; }
  .contact-list svg { flex: none; }
  .back-rule {
    position: absolute; left: 0; right: 0; top: 172px; height: 2px; background: var(--rule);
  }
  .back-url {
    position: absolute; left: 24px; top: 232px;
    font-weight: 700; font-size: 17px; color: var(--teal-text);
  }
</style>
</head>
<body>

<section class="card card-front" aria-label="Business card front">
  <div class="front-showcase">
    <div class="work-photo photo-bag" role="img" aria-label="Photo of a yellow leather bag"></div>
    <div class="work-photo photo-bowl" role="img" aria-label="Photo of a raku ceramic bowl"></div>
    <div class="work-photo photo-pottery" role="img" aria-label="Photo of glazed brown and green pottery cups"></div>
    <div class="work-photo photo-necklace" role="img" aria-label="Photo of a beaded necklace"></div>
  </div>
  <div class="front-band"></div>
  <div class="brand-mark">Woven Glass and Tide</div>
  <p class="front-url">www.Woven Glass and Tide.example</p>
</section>

<section class="card card-back" aria-label="Business card back">
  <div class="brand-mark">Woven Glass and Tide</div>
  <h1 class="holder-name">Helena Pikeworth</h1>
  <p class="holder-title">Designer</p>
  <div class="back-rule"></div>
  <ul class="contact-list">
    <li>
      <svg width="18" height="18" viewBox="0 0 18 18" aria-hidden="true">
        <circle cx="9" cy="9" r="8" fill="none" stroke="#1d1d1d" stroke-width="1.5"/>
        <path d="M6 5.5 l2 0 l0.6 2 l-1.2 0.9 a5 5 0 0 0 2.2 2.2 l0.9-1.2 l2 0.6 l0 2 a6 6 0 0 1-6.5-6.5z" fill="#1d1d1d"/>
      </svg>604.555.0172
    </li>
    <li>
      <svg width="20" height="16" viewBox="0 0 20 16" aria-hidden="true">
        <rect x="1" y="2" width="18" height="12" fill="#ffffff" stroke="#1f9b8e" stroke-width="1.5"/>
        <path d="M1 2 L10 9 L19 2" fill="none" stroke="#1f9b8e" stroke-width="1.5"/>
      </svg>Designer@WovenGlassandTide.example
    </li>
    <li>
      <svg width="18" height="18" viewBox="0 0 18 18" aria-hidden="true">
        <circle cx="9" cy="9" r="8" fill="none" stroke="#1d1d1d" stroke-width="1.5"/>
        <ellipse cx="9" cy="9" rx="3.5" ry="8" fill="none" stroke="#1d1d1d" stroke-width="1.2"/>
        <line x1="1" y1="9" x2="17" y2="9" stroke="#1d1d1d" stroke-width="1.2"/>
      </svg>www.WovenGlassandTide.example
    </li>
    <li>
      <svg width="32" height="16" viewBox="0 0 32 16" aria-hidden="true">
        <rect x="1" y="1" width="30" height="12" rx="2" fill="#1f9b8e"/>
        <text x="16" y="10.5" text-anchor="middle" font-size="8" font-family="Arial, sans-serif" font-weight="700" fill="#ffffff">BLOG</text>
      </svg>www.ShapingHillside.example
    </li>
  </ul>
  <p class="back-url">www.Woven Glass and Tide.example</p>
</section>

</body>
</html>
```